Redesign Current Website Into An Exciting Updated Design

We need to redesign the current website www.glintvaultoffers.net We want an overall new look. We are rebranding so it will be a new logo and we would like to see new images as well so you cannot compare the old from the new.

You can use same exact content as on current url www.glintvaultoffers.net

The website must be warm and inviting and fun yet professional and modern.

The website must also be designed with mobile in mind

The website must be warm and inviting yet professional and modern.

The website must also be designed with mobile in mind.

Target Market(s)

Consumers redeeming rewards

Industry/Entity Type

Promotional Reward Fullfillment

Coding

Coded - Design and coding required

Number of Pages Required

3 page

Requirements
Must have
• This website is a website where consumers come to redeem rewards they received from doing business with a company that offers these rewards. So the website should be very inviting.
Nice to have
• open
Should not have
• open

```html
<!DOCTYPE html>
<html lang="en">
<head>
<meta charset="utf-8">
<title>Bright Token Rewards – Online Redemption System</title>
<link href="https://fonts.googleapis.com/css2?family=Oswald:wght@400;500&family=Jost:ital,wght@0,400;0,500;1,400&display=swap" rel="stylesheet">
<style>
:root{
  --ink:#000;
  --paper:#fff;
  --mint:#1fe8a8;
  --mint-deep:#17c495;
  --card:#e8e8e8;
  --text:#555;
  --line:#333;
}
*{box-sizing:border-box;margin:0;padding:0}
html,body{width:1200px;height:3310px;overflow:hidden}
body{position:relative;background:var(--paper);font-family:'Jost',sans-serif;color:#111}
.abs{position:absolute}
.head-font{font-family:'Oswald',sans-serif;font-weight:400;text-transform:uppercase}
.btn{display:flex;align-items:center;justify-content:center;border-radius:30px;background:linear-gradient(90deg,var(--mint-deep),var(--mint));font-weight:500;font-size:14px;text-transform:uppercase;color:#0b2b22}

.hero{left:0;top:0;width:1200px;height:800px;background:var(--ink)}
.brand{display:flex;align-items:center;gap:10px;color:#fff;font-family:'Jost',sans-serif;font-weight:500;font-size:19px;line-height:22px}
.brand i{width:14px;height:14px;border-radius:50%;background:#fff;display:block;flex:none}
.nav{top:50px;display:flex;gap:34px;left:583px;color:#fff;font-size:12px;text-transform:uppercase;font-weight:500}
.contact-btn{left:956px;top:35px;width:154px;height:45px}
.hero-title{left:90px;top:184px;color:#fff;font-size:66px;line-height:71px}
.hero-title span{color:var(--mint)}
.hero-copy{left:90px;top:409px;width:450px;color:#fff;font-size:13.5px;line-height:22px}
.field{height:47px;border:1.5px solid #fff;border-radius:26px;color:#fff;font-size:13px;display:flex;align-items:center;padding-left:18px}
.go{left:90px;top:569px;width:69px;height:46px}
.hero-photo{left:691px;top:145px;width:419px;height:522px;border-radius:22px;background:linear-gradient(180deg,#4f7a5a 0%,#2aa6b5 45%,#137f8c 70%,#8a4a2a 100%)}
.badge{background:#fff;border-radius:12px;display:flex;align-items:center;gap:16px;padding-left:8px;font-size:13px}
.badge i{width:52px;height:52px;border-radius:50%;background:var(--mint-deep);display:block}

.main{left:0;top:758px;width:1200px;height:2160px;background:var(--paper);border-radius:44px 44px 0 0}
.cat{top:848px;height:220px;background:var(--card);border-radius:24px}
.cat-label{position:absolute;left:14px;bottom:34px;font-size:20px;line-height:26px;color:#111}
.cat svg{position:absolute;left:14px;top:48px}
.cat-photo{position:absolute;left:212px;top:8px;width:186px;height:204px;border-radius:18px;background:linear-gradient(135deg,#f2f2f2,#c9c9c9)}

.section-title{font-size:46px;color:#111}
.body-copy{font-size:12px;line-height:19.6px;color:var(--text)}
.body-copy p+p{margin-top:17px}
.photo{border-radius:26px}
.quote{left:565px;top:2298px}
.testimonial{left:210px;top:2413px;width:780px;text-align:center;font-style:italic;font-size:14px;line-height:27px;color:#555}
.who{left:0;width:1200px;text-align:center;font-size:13px;font-weight:500}
.client{top:2695px;width:224px;height:95px;border:1px solid #ddd;border-radius:4px;display:flex;align-items:center;justify-content:center;gap:10px;font-size:22px;font-weight:500;color:#1a3d7c}

.footer{left:0;top:2887px;width:1200px;height:423px;background:var(--ink);border-radius:44px 44px 0 0;color:#fff}
.f-title{font-size:21px}
.f-links{font-size:12px;line-height:27px}
.f-item{font-size:13px;line-height:18px}
.f-item small{display:block;font-size:12px;color:#ddd}
.social{display:flex;gap:5px}
.social span{width:38px;height:38px;border-radius:50%;background:#222;display:block}
.social span:first-child{background:var(--mint-deep)}
.rule{left:88px;top:3247px;width:1024px;height:1px;background:var(--line)}
.copy{left:0;top:3265px;width:1200px;text-align:center;font-size:13px}
.top-btn{left:1132px;top:3227px;width:40px;height:40px;border-radius:50%;background:var(--mint-deep);display:flex;align-items:center;justify-content:center}
</style>
</head>
<body>

<section class="hero abs">
  <div class="brand abs" style="left:90px;top:35px"><i></i><span>Bright Token<br>Rewards</span></div>
  <nav class="nav abs"><span>Testimonials</span><span>Already Redeemed?</span><span>Help</span></nav>
  <div class="contact-btn btn abs">Contact Us</div>
  <h1 class="hero-title abs head-font">Welcome to the<br>online <span>redemption</span><br>system</h1>
  <p class="hero-copy abs">To Learn More About Your Offer Including The Full Details, How It Works, Terms, FAQ's and To Redeem and Activate Your Certificate Please Enter A Valid Certificate Number and Email.</p>
  <div class="field abs" style="left:90px;top:495px;width:193px">Certificate ID</div>
  <div class="field abs" style="left:294px;top:495px;width:210px">Enter Email Address</div>
  <div class="go btn abs">Go</div>
  <div class="hero-photo abs" role="img" aria-label="Traveller sitting at the bow of a wooden boat among limestone cliffs and turquoise water"></div>
  <div class="badge abs" style="left:595px;top:452px;width:271px;height:62px"><i></i>Exclusive Discounts Await</div>
  <div class="badge abs" style="left:623px;top:527px;width:243px;height:62px"><i></i>Redeem &amp; Enjoy</div>
</section>

<section class="main abs"></section>

<div class="cat abs" style="left:89px;width:404px">
  <svg width="84" height="84" viewBox="0 0 84 84" fill="none" stroke="#17c495" stroke-width="3"><rect x="16" y="38" width="42" height="32"/><path d="M8 76h60M28 38V22h20v16M36 8v14M12 26h16M48 26h16"/><circle cx="36" cy="6" r="3"/><circle cx="10" cy="26" r="3"/><circle cx="66" cy="26" r="3"/></svg>
  <div class="cat-label head-font">Digital<br>Electronic Products</div>
  <div class="cat-photo" role="img" aria-label="Hand holding a tablet showing a greeting on screen"></div>
</div>
<div class="cat abs" style="left:508px;width:140px">
  <svg width="70" height="84" viewBox="0 0 70 84" fill="none" stroke="#17c495" stroke-width="3"><path d="M4 4h40v66H4zM12 16h24M12 26h24M12 36h24M12 46h14"/><circle cx="44" cy="58" r="10"/><path d="M38 66l-4 14 10-5 10 5-4-14"/></svg>
  <div class="cat-label head-font">Vacation<br>Certificates</div>
</div>
<div class="cat abs" style="left:660px;width:142px">
  <svg width="74" height="84" viewBox="0 0 74 84" fill="none" stroke="#17c495" stroke-width="3"><rect x="4" y="36" width="66" height="40"/><rect x="14" y="22" width="46" height="14"/><path d="M37 22v54M37 22c-8-14-20-8-10 0M37 22c8-14 20-8 10 0"/></svg>
  <div class="cat-label head-font">Travel<br>Vouchers</div>
</div>
<div class="cat abs" style="left:816px;width:140px">
  <svg width="70" height="84" viewBox="0 0 70 84" fill="none" stroke="#17c495" stroke-width="3"><circle cx="35" cy="40" r="30"/><circle cx="35" cy="40" r="18"/><path d="M35 30v20M30 35h8a4 4 0 010 8h-6"/></svg>
  <div class="cat-label head-font">Dining<br>Incentives</div>
</div>
<div class="cat abs" style="left:970px;width:140px">
  <svg width="70" height="84" viewBox="0 0 70 84" fill="none" stroke="#17c495" stroke-width="3"><path d="M4 34h60l-6 34H12zM20 34l10-18M48 34l-8-18M22 44v16M34 44v16M46 44v16"/><circle cx="18" cy="76" r="4"/><circle cx="50" cy="76" r="4"/></svg>
  <div class="cat-label head-font">Grocery<br>Rewards</div>
</div>

<h2 class="section-title head-font abs" style="left:125px;top:1184px">About Us</h2>
<div class="body-copy abs" style="left:125px;top:1254px;width:392px">
  <p>We provide marketing incentives in the form of gift certificates and vouchers that are redeemable for a variety of items such as discount travel, smart device products, restaurant incentives , golf discounts and more to thousands of businesses around the world who use them to create exciting marketing promotions and giveaways, customer loyalty programs, promotional contests and use them as customer appreciation gifts.</p>
  <p>We are simply a 3rd party administrator that handles the redemption and fulfillment processing for a variety of incentive gifts and rewards. We have created the platform that facilitates the redemption and fulfillment process in a comprehensive, an easy to use online interface. Simply enter your code and email to redeem your offer and follow the steps to complete the fulfillment process to receive your gift. We work with thousands of large corporations and even small independently owned businesses that trust us to take care of their customers. It's our goal to make it easy for you to redeem your offer.</p>
</div>
<div class="photo abs" style="left:635px;top:1160px;width:440px;height:459px;background:linear-gradient(180deg,#0d3f8c 0%,#3f7fc8 55%,#dfe9f3 100%)" role="img" aria-label="Passenger jet flying above the clouds in a deep blue sky"></div>

<div class="photo abs" style="left:125px;top:1717px;width:440px;height:492px;background:linear-gradient(180deg,#c9d6df 0%,#4d6b3f 40%,#2bb5c4 75%,#f2efe6 100%)" role="img" aria-label="Tropical island peak with overwater bungalows and turquoise lagoon"></div>
<div class="body-copy abs" style="left:635px;top:1742px;width:446px">
  <p>We never market or distribute our incentives to end users as our business model is selling them to businesses and they distribute them to their customers through creative marketing strategies. The only way the recipient can get their hands on one of the certificates and vouchers is by participating in a promotion from one of the thousands of businesses around the world that currently use our marketing incentives in their advertising efforts.</p>
  <p>Since we do not ever distribute certificates to end users and only facilitate the redemption and fulfillment process, we can only honor what is stated in the terms and conditions of the offer. Be sure to read all the details, terms and frequently asked questions regarding your offer to better understand how your offer works. Our vendors, whom we contract with to make these offers happen are responsible for providing the specific terms and conditions in order to use the offer and we simply play as a middle man and a 3rd party administrator to facilitate the fulfillment process while enforcing the requirements. If you ever need to get a hold of us, simply login to the website by entering your certificate number and email at the top of this page and then by clicking on the red Support tab located in the lower right hand corner of your dashboard. We look forward to facilitating the process from start to finish.</p>
</div>
<div class="btn abs" style="left:635px;top:2133px;width:235px;height:45px">Redeem Your Offer Now</div>

<svg class="quote abs" width="72" height="48" viewBox="0 0 72 48"><path d="M18 48a17 17 0 110-34c2-6 8-12 14-14-6 6-8 12-7 16a17 17 0 01-7 32z" fill="#17c495"/><path d="M54 48a17 17 0 110-34c2-6 8-12 14-14-6 6-8 12-7 16a17 17 0 01-7 32z" fill="#1fe8a8"/></svg>
<h2 class="section-title head-font abs" style="left:0;top:2348px;width:1200px;text-align:center">Testimonials</h2>
<p class="testimonial abs">"It was GREAT! I've always wanted to go to Vegas. Being able to stay right on the strip was great. I love that we were able to walk to a lot of the sites. The fountains at the Solvanta were AMAZING! I LOVED the atmosphere and the food. The whole experience was awesome. I would love to return."</p>
<div class="who abs" style="top:2506px">DANA R.</div>
<div class="who abs" style="top:2530px">Pine Hollow, MS</div>

<h2 class="section-title head-font abs" style="left:0;top:2622px;width:1200px;text-align:center">Our Clients</h2>
<div class="client abs" style="left:108px">Northgate Realty</div>
<div class="client abs" style="left:361px">HomeCrate</div>
<div class="client abs" style="left:615px">Veloran Motors</div>
<div class="client abs" style="left:869px">Skyline Vision</div>

<footer class="footer abs">
  <div class="brand abs" style="left:125px;top:120px;font-size:22px;line-height:26px"><i></i><span>Bright Token<br>Rewards</span></div>
  <div class="abs" style="left:400px;top:82px">
    <div class="f-title head-font">Quick Links</div>
    <div class="f-links" style="margin-top:8px">Testimonials<br>Already Redeemed?<br>Help</div>
  </div>
  <div class="abs" style="left:650px;top:82px">
    <div class="f-title head-font">Contact Us</div>
    <div class="f-item" style="margin:10px 0 0 18px">Phone*<small>+08 123 456 7890</small></div>
    <div class="f-item" style="margin:18px 0 0 18px">Email*<small>info@example.com</small></div>
    <div class="f-item" style="margin:18px 0 0 18px">Loction*<small>Some address line<br>goes here city name</small></div>
  </div>
  <svg class="abs" style="left:650px;top:119px" width="12" height="12" viewBox="0 0 12 12"><path d="M2 1l3 0 1 3-2 1a7 7 0 003 3l1-2 3 1v3c-6 1-10-3-9-9z" fill="#17c495"/></svg>
  <svg class="abs" style="left:650px;top:174px" width="12" height="10" viewBox="0 0 12 10"><rect width="12" height="10" fill="#17c495"/><path d="M0 0l6 5 6-5" stroke="#000" fill="none"/></svg>
  <svg class="abs" style="left:651px;top:229px" width="10" height="14" viewBox="0 0 10 14"><path d="M5 14S0 8 0 5a5 5 0 0110 0c0 3-5 9-5 9z" fill="#17c495"/><circle cx="5" cy="5" r="2" fill="#000"/></svg>
  <div class="abs" style="left:906px;top:82px">
    <div class="f-title head-font">Follow Us</div>
    <div class="social" style="margin-top:20px" aria-label="Social profiles"><span></span><span></span><span></span><span></span></div>
  </div>
</footer>
<div class="rule abs"></div>
<div class="copy abs" style="color:#fff">© Copyright 2025 Bright Token Rewards | All rights reserved</div>
<div class="top-btn abs"><svg width="12" height="8" viewBox="0 0 12 8"><path d="M1 7l5-5 5 5" stroke="#fff" stroke-width="2" fill="none"/></svg></div>

</body>
</html>
```